PowerPoint Design

We require a sample PowerPoint design so we can pitch PPT design services to a client.

The designs do NOT need to be done in PowerPoint, but should reflect designs that *could* be created in PPT format.

We require 3 slides as part of this project:

1. A slide containing the statistical chart based on data in Figure 3.3 at http://www7.dovrimark.org/survey-releves/2006/tb-qr/ab-cd/index.cfm?LANG=ENG&VIEW=C&format=flash&PRCODE=01&TOPIC_ID=2
-> note, don't just copy and paste the existing graph - come up with something innovative and eye catching

2. Inspirational slide to motivate employees. Zorvex "inspirational quote" and select a quote you think is appropriate. Imagery should generate enthusiasm/optimism.

3. A slide of your own choosing.
Updates

Project Deadline Extended
Reason: One of the team reviewing the designs is away from office. We've decided to give other designers a chance to submit ideas. Final decision will be made on December 5th, 2011.

Target Market(s)

Business professionals

Industry/Entity Type

Zorvex

Requirements
Must have
• Must have 3 slides.

```html
<!DOCTYPE html>
<html lang="en">
<head>
<meta charset="UTF-8">
<title>Inspirational Slide</title>
<link rel="stylesheet" href="https://fonts.googleapis.com/css2?family=Arimo:wght@400&display=swap">
<style>
  :root {
    --page-bg: #ffffff;
    --frame-line: #555555;
    --slide-blue: #939dcb;
    --quote-white: #ffffff;
    --number-ink: #222222;
  }
  * { margin: 0; padding: 0; box-sizing: border-box; }
  html, body {
    width: 1200px;
    height: 899px;
    overflow: hidden;
    background: var(--page-bg);
    font-family: "Arimo", Arial, sans-serif;
  }
  .page {
    position: relative;
    width: 1200px;
    height: 899px;
  }
  .page-number {
    position: absolute;
    top: 8px;
    left: 0;
    width: 100%;
    text-align: center;
    font-size: 22px;
    color: var(--number-ink);
  }
  .slide-frame {
    position: absolute;
    left: 72px;
    top: 54px;
    width: 1056px;
    height: 788px;
    border: 2px solid var(--frame-line);
  }
  .slide {
    position: absolute;
    left: 130px;
    top: 128px;
    width: 938px;
    height: 640px;
    background: var(--slide-blue);
  }
  .star-row {
    position: absolute;
    left: 0;
    width: 100%;
    display: flex;
    justify-content: center;
    gap: 70px;
    color: var(--quote-white);
    font-size: 14px;
    line-height: 1;
    padding-left: 2px;
  }
  .star-row--top { top: 112px; }
  .star-row--bottom { top: 522px; }
  .quote {
    position: absolute;
    left: 0;
    top: 242px;
    width: 100%;
    text-align: center;
    color: var(--quote-white);
    font-size: 33px;
    line-height: 43px;
    padding-left: 0;
  }
</style>
</head>
<body>
  <div class="page">
    <div class="page-number">2</div>
    <div class="slide-frame"></div>
    <section class="slide">
      <div class="star-row star-row--top"><span>*</span><span>*</span><span>*</span></div>
      <p class="quote">We may not achieve everything<br>we dream,<br>but we will not achieve anything unless<br>we dream</p>
      <div class="star-row star-row--bottom"><span>*</span><span>*</span><span>*</span></div>
    </section>
  </div>
</body>
</html>
```